Brindle Sky Forwarding Website

We require a prominent webpage for a new concept on an old idea. We are a freight forwarding company in the Bahamas that will streamline the import process in the Bahamas for clients while offering both airfreight and seafreight import and export services . We would like the final design to communicate a professional image with stable service offering. Please view www.tovrelfreight.example to see an example of what we require. Also view the site www.pemlo.tariffs.example and quorvin.example. We will requier integration with these and other websites.

Target Market(s)

Small (<100) and medium (100-500) commercial businesses that require full importation services.

Industry/Entity Type

Freight Forwarding

Coding

Coded - Design and coding required

Number of Pages Required

5+ page

Colors

Designer to choose colors to be used in the design.

Requirements
Must have
• Core Website Development – Front End
• 1. Website Design
• 2. Coding and Development
• 4. Graphics
• 5. Social Media Integrations
• 6. Email Integration
• 7. Security / SSL Integrations
• 8. User Dashboard / Account
• 9. Customer Signup Integration
• 10. eCommerceOnlinePayment
• 11. XML–APIDevelopmentforQuorvin
• 12. QuorvinIntegrations

```html
<!DOCTYPE html>
<html lang="en">
<head>
<meta charset="utf-8">
<title>Brindle Sky Forwarding</title>
<link href="https://fonts.googleapis.com/css2?family=Merriweather:wght@400;700&family=Open+Sans:wght@400;600;700&display=swap" rel="stylesheet">
<style>
:root{
  --navy:#1c3557;
  --navy-dark:#0f1d31;
  --teal:#2f86a6;
  --red:#d0242b;
  --ink:#3a3f47;
  --muted:#6b7280;
  --light:#f1f2f4;
  --white:#ffffff;
}
*{box-sizing:border-box;margin:0;padding:0}
html,body{width:1200px;height:3048px;overflow:hidden}
body{font-family:"Open Sans",Arial,sans-serif;color:var(--ink);background:var(--white);position:relative}
.nav{position:absolute;left:0;top:0;width:1200px;height:72px;display:flex;align-items:center;justify-content:center;background:var(--white)}
.nav a{font-family:"Merriweather",Georgia,serif;font-size:16px;color:var(--navy);text-decoration:none;margin:0 38px}
.brand{display:flex;align-items:center;gap:8px;margin:0 40px}
.brand-dot{width:18px;height:18px;border-radius:50%;background:var(--red)}
.brand-name{font-family:"Merriweather",Georgia,serif;font-weight:700;font-size:15px;color:var(--navy);white-space:nowrap}
.hero{position:absolute;left:0;top:72px;width:1200px;height:640px;background:linear-gradient(180deg,#2a3446 0%,#1b2230 55%,#3a2a24 100%);text-align:center}
.hero-title{position:absolute;top:210px;left:0;width:100%;font-family:"Merriweather",Georgia,serif;font-weight:700;font-size:58px;line-height:70px}
.hero-title .accent{color:var(--teal)}
.hero-title .plain{color:var(--white)}
.hero-text{position:absolute;top:360px;left:260px;width:680px;color:#e6e9ee;font-size:15px;line-height:24px}
.btn{position:absolute;top:432px;left:551px;width:98px;height:38px;line-height:38px;border-radius:4px;background:var(--red);color:var(--white);font-size:13px;font-weight:600}
.dots{position:absolute;top:602px;left:0;width:100%;display:flex;justify-content:center;gap:14px}
.dots span{width:10px;height:10px;border-radius:50%;background:#8a93a3}
.dots span:first-child{background:var(--white)}
.section-title{position:absolute;left:0;width:1200px;text-align:center;font-family:"Merriweather",Georgia,serif;font-size:32px;color:var(--navy)}
.intro{position:absolute;top:858px;left:160px;width:880px;text-align:center;font-size:13px;line-height:22px;color:var(--muted)}
.service{position:absolute;width:520px}
.service h3{font-family:"Merriweather",Georgia,serif;font-size:17px;color:var(--navy);margin-bottom:20px}
.service p{font-size:13px;line-height:22px;color:var(--muted)}
.photo{position:absolute;width:380px;height:380px}
.photo .fill{position:absolute;left:30px;top:30px;width:320px;height:320px;border-radius:50%;border:6px solid var(--white);box-shadow:0 0 0 2px #d7dbe1}
.contact{position:absolute;top:2336px;left:0;width:1200px;height:512px;background:var(--light)}
.contact-icon{position:absolute;top:112px;left:588px;width:24px;height:24px;border-radius:50%;background:var(--navy)}
.map{position:absolute;top:176px;left:150px;width:490px;height:262px;background:linear-gradient(135deg,#cfe3f2 0%,#b8d4e8 45%,#dcd8c8 60%,#e7e3d6 100%)}
.address{position:absolute;left:672px;width:400px;border-left:3px solid var(--red);padding-left:18px}
.address h4{font-family:"Merriweather",Georgia,serif;font-size:16px;color:var(--navy);margin-bottom:10px}
.address p{font-size:12px;line-height:20px;color:var(--muted)}
.footer-nav{position:absolute;top:2862px;left:0;width:1200px;display:flex;justify-content:center;align-items:center}
.footer-nav a{font-family:"Merriweather",Georgia,serif;font-size:16px;color:var(--navy);text-decoration:none;margin:0 38px}
.copyright{position:absolute;top:2972px;left:0;width:1200px;text-align:center;font-size:14px;color:var(--ink)}
.rule{position:absolute;top:2940px;left:0;width:1200px;height:1px;background:#e1e4e8}
</style>
</head>
<body>

<nav class="nav">
  <a href="#">Home</a><a href="#">About Us</a><a href="#">Services</a>
  <div class="brand"><span class="brand-dot"></span><span class="brand-name">Brindle Sky Forwarding</span></div>
  <a href="#">Faqs</a><a href="#">Clients</a><a href="#">Contact Us</a>
</nav>

<header class="hero" role="img" aria-label="Cargo ship at port with an airplane overhead at dusk">
  <h1 class="hero-title"><span class="accent">YourForwarding</span><br><span class="plain">SolutionsProvider!!</span></h1>
  <p class="hero-text">Our mission is to constantly exceed customer expectations by providing superior freight forwarding and global transportation solutions including customs clearance and logistics services.</p>
  <a class="btn">Learn More</a>
  <div class="dots"><span></span><span></span><span></span><span></span></div>
</header>

<h2 class="section-title" style="top:782px">Services</h2>
<svg style="position:absolute;top:826px;left:540px" width="120" height="10" viewBox="0 0 120 10"><path d="M0 8 Q60 -4 120 8" fill="none" stroke="var(--red)" stroke-width="2"/></svg>
<p class="intro">We strive to import every shipment quickly and reliably for all clients, whether shipping by air or by sea. Our experienced team handles every step, from booking and paperwork through customs release and final delivery to your door.</p>

<!-- Service 1 -->
<div class="service" style="top:1010px;left:152px">
  <h3>Freight Forwarding &amp; Logistics</h3>
  <p>We offer freight forwarding and logistics services that include international freight forwarding, import and export of all cargo types by air and by sea. Our team plans each route to meet your time and budget needs, and our network of trusted carriers keeps your goods moving safely and on schedule from origin to delivery.</p>
</div>
<div class="photo" style="top:972px;left:730px">
  <svg width="380" height="380" viewBox="0 0 380 380" style="position:absolute;left:0;top:0"><path d="M40 250 A160 160 0 0 1 190 20" fill="none" stroke="var(--red)" stroke-width="6"/><path d="M330 120 A160 160 0 0 1 200 360" fill="none" stroke="var(--navy)" stroke-width="6"/></svg>
  <div class="fill" role="img" aria-label="Red freight truck with cargo plane in the sky" style="background:linear-gradient(160deg,#e9eef4 0%,#c9d3de 50%,#b3262c 100%)"></div>
</div>

<!-- Service 2 -->
<div class="photo" style="top:1290px;left:150px">
  <svg width="380" height="380" viewBox="0 0 380 380" style="position:absolute;left:0;top:0"><path d="M190 20 A160 160 0 0 1 340 240" fill="none" stroke="var(--red)" stroke-width="6"/><path d="M50 120 A160 160 0 0 0 180 360" fill="none" stroke="var(--navy)" stroke-width="6"/></svg>
  <div class="fill" role="img" aria-label="Trucks on a highway at sunset" style="background:linear-gradient(170deg,#3b3f7a 0%,#8a4f8c 45%,#e69a4f 75%,#2a2f45 100%)"></div>
</div>
<div class="service" style="top:1330px;left:620px">
  <h3>Freight Consolidation Services</h3>
  <p>Our consolidation service lets shipments share space with others to fill a standard container, lowering the cost of shipping for smaller orders. We collect goods from many suppliers, combine them at our warehouse and ship them together, then sort and release each order once it clears customs.</p>
</div>

<!-- Service 3 -->
<div class="service" style="top:1670px;left:152px">
  <h3>Customs Clearance Services</h3>
  <p>We offer customs clearance services that include preparation of entries, duty calculation and filing with the local tariff office for all cargo types by air and by sea. Our brokers track every rule change, so your goods are released without delay and you pay only what is owed.</p>
</div>
<div class="photo" style="top:1630px;left:730px">
  <svg width="380" height="380" viewBox="0 0 380 380" style="position:absolute;left:0;top:0"><path d="M40 250 A160 160 0 0 1 190 20" fill="none" stroke="var(--red)" stroke-width="6"/><path d="M330 120 A160 160 0 0 1 200 360" fill="none" stroke="var(--navy)" stroke-width="6"/></svg>
  <div class="fill" role="img" aria-label="Worker in red uniform beside stacked shipping containers" style="background:linear-gradient(180deg,#dfe6ee 0%,#9fb3c8 45%,#c0392b 100%)"></div>
</div>

<!-- Service 4 -->
<div class="photo" style="top:1912px;left:150px">
  <svg width="380" height="380" viewBox="0 0 380 380" style="position:absolute;left:0;top:0"><path d="M190 20 A160 160 0 0 1 340 240" fill="none" stroke="var(--red)" stroke-width="6"/><path d="M50 120 A160 160 0 0 0 180 360" fill="none" stroke="var(--navy)" stroke-width="6"/></svg>
  <div class="fill" role="img" aria-label="Warehouse worker in hard hat and safety vest holding a clipboard" style="background:linear-gradient(170deg,#c7b79a 0%,#8c7a5e 50%,#b9cf3a 100%)"></div>
</div>
<div class="service" style="top:2012px;left:620px">
  <h3>Warehousing</h3>
  <p>We offer dedicated warehousing services to our clients that helps them do easy handling of their imports and exports with safe storage and quick access, along with secure pickup and delivery anytime they need it.</p>
</div>

<section class="contact">
  <h2 class="section-title" style="top:54px">Contact Us</h2>
  <div class="contact-icon"></div>
  <div class="map" role="img" aria-label="Map of the island showing the office location"></div>
  <div class="address" style="top:190px">
    <h4>Bahamas Address</h4>
    <p>P.O. Box SK-4417, Harbour Row, Nassau<br>(242) 555-0142 | (242) 555-0187<br>bahamas@brindleskyfreight.example</p>
  </div>
  <div class="address" style="top:322px">
    <h4>US Address</h4>
    <p>2250 Corvale Way, Suite 12, Miami, FL 33100<br>(305) 555-0163<br>usoffice@brindleskyfreight.example</p>
  </div>
</section>

<nav class="footer-nav">
  <a href="#">Home</a><a href="#">About Us</a><a href="#">Services</a>
  <div class="brand"><span class="brand-dot"></span><span class="brand-name">Brindle Sky Forwarding</span></div>
  <a href="#">Faqs</a><a href="#">Clients</a><a href="#">Contact Us</a>
</nav>
<div class="rule"></div>
<p class="copyright">© 2019 Company Name &nbsp;|&nbsp; All Rights Reserved</p>

</body>
</html>
```